Vell Partners Building Business Cards

We need a business card that reflects our business as "Solar Experts" in San Diego. Browse our website www.vellpartners.example our License needs to be displayed as "CSLB# 4718392" our phone number is (619) 555-0147

Save thousands on your electric bills and increase the value of your home while helping to protect the environment. Our solar installation experts will help you design the system that's right for you, using only the highest quality equipment that will look great and give you ideal performance. Our goal is to make you energy independent, and get your electric bill to 0.

Tobias Wrenfield
(619) 555-0147
tobias@vellpartners.example

Target Market(s)

Home owners in san diego looking for solar

Industry/Entity Type

Solar Energy

Contact Information for Business Card

Tobias Wrenfield
(619) 555-0147
tobias@vellpartners.example

Font styles to use
Other font styles liked:
• Use our logo font

Requirements
Must have
• License needs to be displayed as "CSLB# 4718392" our phone number is (619) 555-0147
Nice to have
• Real images of rooftop home solar in san diego
Should not have
• our business address

```html
<!DOCTYPE html>
<html lang="en">
<head>
<meta charset="utf-8">
<title>Vell Partners Building – Business Cards</title>
<link rel="stylesheet" href="https://fonts.googleapis.com/css2?family=Montserrat:wght@600;800&display=swap">
<style>
  :root {
    --brand-blue: #1e4f95;
    --brand-blue-deep: #174282;
    --sun-yellow: #f4ac1c;
    --paper: #ffffff;
    --backdrop: #2a2a2c;
    --photo-light: #eef0f2;
    --photo-mid: #c9ced4;
  }
  * { box-sizing: border-box; margin: 0; padding: 0; }
  html, body { width: 1200px; height: 900px; overflow: hidden; }
  body {
    background: var(--backdrop);
    font-family: "Montserrat", Arial, sans-serif;
    position: relative;
  }
  .card {
    position: absolute;
    width: 620px;
    height: 354px;
    border-radius: 34px;
    overflow: hidden;
  }
  .card--front {
    left: 150px; top: 70px;
    background: var(--brand-blue);
    display: flex; align-items: center; justify-content: center;
  }
  .card--back {
    left: 430px; top: 476px;
    background: var(--brand-blue);
  }
  .wordmark {
    font-weight: 800;
    font-size: 42px;
    letter-spacing: -0.5px;
    line-height: 1;
  }
  .card--front .wordmark { color: var(--paper); }
  .rooftop-photo {
    position: absolute; left: 0; top: 0; width: 100%; height: 190px;
    background: linear-gradient(120deg, var(--photo-light) 0%, var(--photo-mid) 55%, var(--photo-light) 100%);
  }
  .card--back .wordmark {
    position: absolute; left: 0; right: 0; top: 82px;
    text-align: center; color: var(--brand-blue);
    font-size: 40px;
  }
  .person {
    position: absolute; left: 40px; bottom: 38px;
  }
  .person__name {
    color: var(--paper); font-weight: 800; font-size: 30px; line-height: 1.1;
  }
  .person__title {
    color: var(--sun-yellow); font-weight: 600; font-size: 19px; margin-top: 4px;
  }
  .divider {
    position: absolute; left: 370px; top: 212px; width: 3px; height: 82px;
    background: var(--sun-yellow);
  }
  .contact-list {
    position: absolute; left: 388px; top: 212px; list-style: none;
    color: var(--paper); font-weight: 600; font-size: 13.5px;
  }
  .contact-list li {
    display: flex; align-items: center; gap: 9px; height: 27px;
  }
  .contact-list svg { width: 15px; height: 15px; flex: none; }
</style>
</head>
<body>
  <section class="card card--front" aria-label="Card front">
    <span class="wordmark">Vell Partners Building</span>
  </section>

  <section class="card card--back" aria-label="Card back">
    <div class="rooftop-photo" role="img" aria-label="Faded photo of solar panels on a home rooftop"></div>
    <span class="wordmark">Vell Partners Building</span>

    <div class="person">
      <p class="person__name">Tobias Wrenfield</p>
      <p class="person__title">Solar Expert</p>
    </div>

    <div class="divider"></div>

    <ul class="contact-list">
      <li>
        <svg viewBox="0 0 16 16" aria-hidden="true"><path fill="#fff" d="M3.5 1.5l2.2 2.8-1.3 1.6c.9 2 2.6 3.7 4.7 4.7l1.6-1.3 2.8 2.2-1.3 2.2C7.4 13.4 2.6 8.6 1.3 2.8z"/></svg>
        (619) 555-0147
      </li>
      <li>
        <svg viewBox="0 0 16 16" aria-hidden="true"><rect x="1.5" y="3.5" width="13" height="9" fill="none" stroke="#fff" stroke-width="1.4"/><path d="M1.5 3.5L8 9l6.5-5.5" fill="none" stroke="#fff" stroke-width="1.4"/></svg>
        tobias@vellpartners.example
      </li>
      <li>
        <svg viewBox="0 0 16 16" aria-hidden="true"><rect x="1.5" y="3" width="13" height="10" rx="1" fill="none" stroke="#fff" stroke-width="1.4"/><rect x="3.5" y="6" width="3.5" height="4" fill="#fff"/><path d="M8.5 6.5h4M8.5 9.5h4" stroke="#fff" stroke-width="1.2"/></svg>
        CSLB# 4718392
      </li>
    </ul>
  </section>
</body>
</html>
```